Retractable Banner Stands

Hello we need a deisgn for a banner.
Sizes: 36"x80", 12"x17"(this one to have less on it, most the logo, license numvber, and address), and a 24"x40" banner
Roofing Services
HOA & Commercial Roofing
• Emergency roof tarping & repairs — Starting at $550
• Small & large roof repairs
• Preventative roof maintenance
• Full roof replacement
Deck & Balcony Services
• Balcony & deck maintenance
SB-326 Repairs
• Deck resurfacing
• Small & large deck repairs
• Full deck reconstruction
Gutter Services
• Small & large gutter repairs
• Gutter cleaning & maintenance
• New gutter installation & replacement
License Information:
C-39 Roofing Contractor
General B Contractor
License #4529730
📍 Serving Orange County & Surrounding Areas
📍 Office Location:
41 Dunwick Street, Suite F
Target Market(s)
HOA & Commerical roofs
Industry/Entity Type
Roofing
Other font styles liked:
- Gotham
Look and feel

```html
<!DOCTYPE html>
<html lang="en">
<head>
<meta charset="UTF-8">
<title>Kestrel Roofing &amp; Waterproofing – Roofing Services Banner</title>
<link href="https://fonts.googleapis.com/css2?family=Montserrat:wght@600;700;800&display=swap" rel="stylesheet">
<style>
  :root {
    --navy: #1d2a3b;
    --navy-deep: #172230;
    --navy-panel: #1c3a5e;
    --sky: #1fa4de;
    --sky-light: #4cbdf0;
    --white: #ffffff;
    --photo-sky: #d9e2e8;
    --photo-house: #b9c2c4;
    --photo-green: #6f7d55;
    --photo-tile: #7b5a45;
    --photo-tile-dark: #3e2f27;
    --pin: #e0352b;
  }
  html, body {
    margin: 0;
    padding: 0;
    width: 833px;
    height: 1200px;
    overflow: hidden;
    background: var(--navy);
  }
  .banner {
    position: relative;
    width: 833px;
    height: 1200px;
    overflow: hidden;
    background: var(--navy);
    font-family: "Montserrat", "Helvetica Neue", Arial, sans-serif;
    color: var(--white);
  }
  .backdrop {
    position: absolute;
    inset: 0;
  }
  .brand-badge {
    position: absolute;
    left: -20px;
    top: -60px;
    width: 380px;
    height: 380px;
    border-radius: 50%;
    background: var(--white);
    display: flex;
    flex-direction: column;
    align-items: center;
    justify-content: center;
    padding-top: 60px;
    box-sizing: border-box;
  }
  .brand-name {
    font-weight: 800;
    font-size: 52px;
    color: var(--navy);
    letter-spacing: 2px;
    line-height: 1;
    margin-left: 20px;
  }
  .brand-tag {
    font-weight: 700;
    font-size: 15px;
    color: var(--navy);
    letter-spacing: 0.5px;
    margin-top: 10px;
    margin-left: 20px;
    text-transform: uppercase;
  }
  .headline {
    position: absolute;
    top: 665px;
    left: 0;
    width: 100%;
    margin: 0;
    text-align: center;
    font-weight: 800;
    font-size: 82px;
    line-height: 1;
    letter-spacing: -0.5px;
  }
  .service-area {
    position: absolute;
    top: 758px;
    left: 60px;
    width: 713px;
    height: 50px;
    background: var(--sky);
    display: flex;
    align-items: center;
    justify-content: center;
    font-weight: 700;
    font-size: 26px;
  }
  .license-title {
    position: absolute;
    top: 838px;
    left: 0;
    width: 100%;
    margin: 0;
    text-align: center;
    color: var(--sky-light);
    font-weight: 700;
    font-size: 38px;
  }
  .license-panel {
    position: absolute;
    top: 912px;
    left: 60px;
    width: 713px;
    height: 186px;
    background: var(--navy-panel);
    display: flex;
    flex-direction: column;
    align-items: center;
    justify-content: center;
    gap: 2px;
  }
  .license-line {
    font-weight: 800;
    font-size: 43px;
    line-height: 1.15;
  }
  .office {
    position: absolute;
    top: 1122px;
    left: 58px;
    right: 40px;
    display: flex;
    align-items: center;
    gap: 12px;
    font-weight: 700;
    font-size: 30px;
    white-space: nowrap;
  }
  .office svg { flex: none; }
</style>
</head>
<body>
<main class="banner">
  <svg class="backdrop" width="833" height="1200" viewBox="0 0 833 1200">
    <defs>
      <linearGradient id="roofPhoto" x1="1" y1="0" x2="0.15" y2="1">
        <stop offset="0" stop-color="var(--photo-sky)"/>
        <stop offset="0.18" stop-color="var(--photo-house)"/>
        <stop offset="0.38" stop-color="var(--photo-green)"/>
        <stop offset="0.58" stop-color="var(--photo-tile)"/>
        <stop offset="1" stop-color="var(--photo-tile-dark)"/>
      </linearGradient>
    </defs>
    <polygon points="0,1200 260,1200 0,960" fill="var(--navy-deep)"/>
    <polygon points="833,600 833,1000 560,650" fill="var(--navy-deep)" opacity="0.6"/>
    <polygon points="0,0 833,0 833,600 540,640 0,490" fill="url(#roofPhoto)" role="img" aria-label="Photo of a roofer in a safety helmet working on a clay tile roof"/>
    <polygon points="0,490 540,640 0,540" fill="var(--navy-deep)"/>
    <polygon points="380,612 833,560 833,600 540,640" fill="var(--sky)"/>
    <polygon points="833,600 833,650 600,632" fill="var(--sky-light)"/>
  </svg>

  <div class="brand-badge">
    <span class="brand-name">KESTREL</span>
    <span class="brand-tag">Roofing &amp; Waterproofing</span>
  </div>

  <h1 class="headline">Roofing Services</h1>
  <div class="service-area">Serving Orange County &amp; Surrounding Areas</div>

  <h2 class="license-title">License Information:</h2>
  <div class="license-panel">
    <span class="license-line">C-39 Roofing Contractor</span>
    <span class="license-line">General B Contractor</span>
    <span class="license-line">License #4529730</span>
  </div>

  <div class="office">
    <svg width="26" height="36" viewBox="0 0 28 38" aria-hidden="true">
      <path d="M14 0C6.3 0 0 6.2 0 13.9 0 24.3 14 38 14 38s14-13.7 14-24.1C28 6.2 21.7 0 14 0z" fill="var(--pin)"/>
      <circle cx="14" cy="13.5" r="5.5" fill="var(--navy)"/>
    </svg>
    <span>Office Location:41 Dunwick Street, Suite F</span>
  </div>
</main>
</body>
</html>
```